Livestream Into Sprint Blueprints Book Cover Design

I need a book cover created that is similar to books created by Gavin Thorley. I will provide examples of those below. Pixelmart Codes, Harbor Lessons, Lantern Rules.

The winner will be selected with 72 hours after 7 days of incoming submissions with GUARANTEED FUNDS.

The color scheme will be a mixture of our two brands of sky blue and money green. That will also be provided. Also I will provide pictures from the two authors of the book that can be placed on the front cover.

```html
<!DOCTYPE html>
<html lang="en">
<head>
<meta charset="utf-8">
<title>Livestream Into Sprint Blueprints — Book Cover</title>
<link rel="stylesheet" href="https://fonts.googleapis.com/css2?family=Anton&family=Montserrat:wght@600;700;800&display=swap">
<style>
  :root {
    --money-green: #52ad63;
    --sky-blue: #1ea8d0;
    --ink: #000000;
    --paper: #ffffff;
    --photo-light: #3a3a3a;
    --photo-mid: #1a1a1a;
    --photo-deep: #0a0a0a;
  }
  * { margin: 0; padding: 0; box-sizing: border-box; }
  html, body { width: 800px; height: 1200px; overflow: hidden; background: var(--ink); }
  .cover {
    position: relative;
    width: 800px;
    height: 1200px;
    background: var(--ink);
    font-family: "Montserrat", sans-serif;
    color: var(--paper);
    overflow: hidden;
  }
  .tagline-band {
    position: absolute; left: 0; top: 0;
    width: 800px; height: 128px;
    background: var(--money-green);
    display: flex; align-items: center; justify-content: center;
  }
  .tagline {
    font-weight: 700;
    font-size: 32px;
    letter-spacing: 4px;
    color: var(--paper);
    line-height: 1;
    white-space: nowrap;
  }
  .author-photos {
    position: absolute; left: 0; top: 590px;
    width: 800px; height: 490px;
    background:
      radial-gradient(ellipse 220px 260px at 215px 300px, rgba(90,90,90,0.55), rgba(0,0,0,0) 100%),
      radial-gradient(ellipse 240px 270px at 615px 300px, rgba(90,90,90,0.55), rgba(0,0,0,0) 100%),
      radial-gradient(ellipse 520px 300px at 560px 120px, var(--photo-light), rgba(0,0,0,0) 100%),
      linear-gradient(180deg, var(--photo-mid) 0%, #151515 55%, var(--photo-deep) 85%, var(--ink) 100%);
  }
  .author-photos::before {
    content: "";
    position: absolute; left: 0; top: 0; width: 100%; height: 40px;
    background: linear-gradient(180deg, var(--ink), rgba(0,0,0,0));
  }
  .title-art {
    position: absolute; left: 0; top: 150px;
    width: 800px; height: 450px;
  }
  .title-word { font-family: "Anton", sans-serif; }
  .title-link {
    font-family: "Montserrat", sans-serif;
    font-weight: 700;
  }
  .byline {
    position: absolute; left: 0; top: 1094px;
    width: 800px; text-align: center;
  }
  .byline-credit {
    font-weight: 700;
    font-size: 16px;
    letter-spacing: 0.2px;
    line-height: 1;
  }
  .byline-name {
    margin-top: 10px;
    font-weight: 700;
    font-size: 46px;
    letter-spacing: 0.5px;
    line-height: 1;
  }
</style>
</head>
<body>
<main class="cover">
  <header class="tagline-band">
    <p class="tagline">EVERYONE NEEDS A LIVESTREAM</p>
  </header>

  <div class="author-photos" role="img" aria-label="Portrait photo of the two authors side by side in front of a dark background with faint business chart graphics"></div>

  <svg class="title-art" viewBox="0 150 800 450" xmlns="http://www.w3.org/2000/svg" role="img" aria-label="Livestream Into Sprint Blueprints">
    <defs>
      <linearGradient id="grad-green-to-blue" x1="0" y1="166" x2="0" y2="325" gradientUnits="userSpaceOnUse">
        <stop offset="0" stop-color="#56b062"/>
        <stop offset="0.55" stop-color="#2aa9b0"/>
        <stop offset="1" stop-color="#1ea8d0"/>
      </linearGradient>
      <linearGradient id="grad-blue-to-green" x1="0" y1="423" x2="0" y2="584" gradientUnits="userSpaceOnUse">
        <stop offset="0" stop-color="#1ea8d0"/>
        <stop offset="0.45" stop-color="#2aa9b0"/>
        <stop offset="1" stop-color="#56b062"/>
      </linearGradient>
      <linearGradient id="rule-fade" x1="0" y1="0" x2="1" y2="0">
        <stop offset="0" stop-color="#52ad63" stop-opacity="0"/>
        <stop offset="0.5" stop-color="#52ad63" stop-opacity="1"/>
        <stop offset="1" stop-color="#52ad63" stop-opacity="0"/>
      </linearGradient>
    </defs>

    <text class="title-word" x="107" y="325" font-size="214" textLength="577" lengthAdjust="spacingAndGlyphs" fill="url(#grad-green-to-blue)">LIVESTREAM</text>

    <rect x="120" y="345" width="560" height="2" fill="url(#rule-fade)"/>
    <text class="title-link" x="126" y="393" font-size="49" textLength="540" lengthAdjust="spacing" fill="#1ea8d0">INTO SPRINT</text>
    <rect x="120" y="405" width="560" height="2" fill="url(#rule-fade)"/>

    <text class="title-word" x="124" y="584" font-size="216" textLength="542" lengthAdjust="spacingAndGlyphs" fill="url(#grad-blue-to-green)">BLUEPRINTS</text>
  </svg>

  <footer class="byline">
    <p class="byline-credit">CREATOR OF THE BROADCAST METHOD GRID</p>
    <p class="byline-name">AUTHOR’S NAME</p>
  </footer>
</main>
</body>
</html>
```